Kereru Valley Alpine Fellowship needs a business card design

We need a business card design for our newly incorporated KVAF. We are helping the NZ Chinese community, as well as everyone else, to organise ski & snowboarding trips, training, and equipments. The design should be creative, energetic, young and vibrant.

Industry/Entity Type

Social Club

Contact Information for Business Card

Logo; Kereru Valley Alpine Fellowship; Name: Mark Dorran; Position: President; Address: 42 Pellow Rd, Kowhai Heights, Tarnwick 4817; Mobile: 020 7591 2284; Email: mark@kvaf-club.example; Web: www.kvaf-club.example

Requirements
Must have
• 1, The text "Kereru Valley Alpine Fellowship" should be put together with the supplied logo file to form a new complete logo combination.
• 2, Final design files should be in Adobe Illustrator format and all text must be editable.
Nice to have
• two or three colours

```html
<!DOCTYPE html>
<html lang="en">
<head>
<meta charset="utf-8">
<title>Kereru Valley Alpine Fellowship – Business Card</title>
<link href="https://fonts.googleapis.com/css2?family=Oswald:wght@600&family=Work+Sans:wght@400;500;700&display=swap" rel="stylesheet">
<style>
  :root {
    --sky: #1aa9df;
    --navy: #1d3f8f;
    --ink: #3a3a3a;
    --paper: #ffffff;
    --backdrop: #d9d9d9;
  }
  * { box-sizing: border-box; margin: 0; padding: 0; }
  html, body { width: 1200px; height: 1000px; overflow: hidden; }
  body {
    background: var(--backdrop);
    font-family: "Work Sans", Arial, sans-serif;
    position: relative;
  }
  .card {
    position: absolute;
    left: 250px;
    width: 700px;
    height: 400px;
    box-shadow: 0 6px 18px rgba(0,0,0,0.25);
    overflow: hidden;
  }
  .card--back { top: 70px; background: var(--paper); }
  .card--front { top: 530px; background: var(--sky); }

  .lockup { position: absolute; left: 48px; top: 58px; display: flex; align-items: center; gap: 14px; }
  .lockup__mark { display: flex; align-items: center; gap: 8px; }
  .lockup__dot { width: 22px; height: 22px; border-radius: 50%; background: var(--navy); }
  .lockup__initials { font-family: "Work Sans", Arial, sans-serif; font-weight: 700; font-size: 42px; color: var(--navy); letter-spacing: 1px; }
  .lockup__name {
    font-family: "Oswald", "Arial Narrow", sans-serif; font-weight: 600;
    font-size: 15px; line-height: 1.15; color: var(--navy); text-transform: uppercase;
    margin-top: 14px;
  }

  .person { position: absolute; left: 48px; top: 196px; }
  .person__name { font-size: 21px; font-weight: 500; color: var(--sky); text-transform: uppercase; letter-spacing: 0.5px; }
  .person__role { font-size: 16px; color: var(--ink); margin-top: 2px; }

  .band { position: absolute; left: 0; right: 0; top: 262px; bottom: 0; background: var(--sky); }
  .band__notch { position: absolute; left: 56px; top: -1px; width: 0; height: 0;
    border-left: 10px solid transparent; border-right: 10px solid transparent; border-top: 11px solid var(--paper); }

  .contacts { position: absolute; left: 48px; top: 30px; list-style: none; }
  .contacts li { display: flex; align-items: center; gap: 14px; color: var(--paper); font-size: 15px; height: 24px; }
  .contacts svg { width: 13px; height: 13px; fill: var(--navy); flex: none; }

  .address { position: absolute; right: 44px; top: 28px; text-align: right; color: var(--navy); font-size: 15px; line-height: 1.55; font-style: normal; }

  .front-logo { position: absolute; left: 0; right: 0; top: 100px; text-align: center; }
  .front-logo__mark { display: inline-flex; align-items: center; gap: 14px; }
  .front-logo__dot { width: 40px; height: 40px; border-radius: 50%; background: var(--navy); }
  .front-logo__initials { font-family: "Work Sans", Arial, sans-serif; font-weight: 700; font-size: 96px; line-height: 1; color: var(--navy); letter-spacing: 2px; }
  .front-logo__name {
    font-family: "Oswald", "Arial Narrow", sans-serif; font-weight: 600; font-size: 30px;
    line-height: 1.1; color: var(--paper); text-transform: uppercase; margin-top: 16px; letter-spacing: 1px;
  }
</style>
</head>
<body>
  <section class="card card--back">
    <div class="lockup">
      <div class="lockup__mark">
        <span class="lockup__dot"></span>
        <span class="lockup__initials">KVAF</span>
      </div>
      <div class="lockup__name">Kereru Valley Alpine<br>Fellowship</div>
    </div>

    <div class="person">
      <div class="person__name">Mark Dorran</div>
      <div class="person__role">President</div>
    </div>

    <div class="band">
      <span class="band__notch"></span>
      <ul class="contacts">
        <li><svg viewBox="0 0 24 24"><path d="M6.6 10.8a15.1 15.1 0 0 0 6.6 6.6l2.2-2.2c.3-.3.7-.4 1-.2 1.1.4 2.3.6 3.6.6.6 0 1 .4 1 1V20c0 .6-.4 1-1 1A17 17 0 0 1 3 4c0-.6.4-1 1-1h3.5c.6 0 1 .4 1 1 0 1.2.2 2.4.6 3.6.1.3 0 .7-.2 1z"/></svg>020 7591 2284</li>
        <li><svg viewBox="0 0 24 24"><path d="M2 5h20v14H2z M2 5l10 8 10-8" fill="none" stroke="#1d3f8f" stroke-width="2.5"/></svg>mark@kvaf-club.example</li>
        <li><svg viewBox="0 0 24 24"><circle cx="12" cy="12" r="10"/></svg>www.kvaf-club.example</li>
      </ul>
      <address class="address">
        Our Residence Address:<br>
        42 Pellow Rd,<br>
        Kowhai Heights, Tarnwick 4817
      </address>
    </div>
  </section>

  <section class="card card--front">
    <div class="front-logo">
      <div class="front-logo__mark">
        <span class="front-logo__dot"></span>
        <span class="front-logo__initials">KVAF</span>
      </div>
      <div class="front-logo__name">Kereru Valley Alpine<br>Fellowship</div>
    </div>
  </section>
</body>
</html>
```